Business Card
Maple Ridge Landscaping
Simple
Derek Holt
Owner/Operator
P.O. Box 917
Cedar Cove, NL
B2K 3M5
mapleridgelndscpg@inboxmail.example
http://maple-ridge-lawncare.example
On the front of card I would like to keep it as simple as possible, probably just business name and logo. Although other designs will be considered
On the back of the card is where I would like to have my information. Centered at the top "Professional Property Maintenance" then underneath that, the slogan "From weeds to winter, we'll take care of your property". Again, any variations on that slogan will be considered, its just a thought in process.

```html
<!DOCTYPE html>
<html lang="en">
<head>
<meta charset="utf-8">
<title>Maple Ridge Landscaping – Business Card</title>
<link href="https://fonts.googleapis.com/css2?family=Open+Sans:wght@400;600&display=swap" rel="stylesheet">
<style>
  :root {
    --page: #e9e6e1;
    --card-black: #0b0b0b;
    --card-charcoal: #1c1c1c;
    --gold: #d9a520;
    --gold-light: #f4d46a;
    --gold-deep: #a87812;
    --silver: #cfcfcf;
    --white: #ffffff;
    --text-muted: #e6e6e6;
  }
  * { margin: 0; padding: 0; box-sizing: border-box; }
  html, body {
    width: 1200px; height: 780px; overflow: hidden;
    background: var(--page);
  }
  .card {
    position: absolute; left: 60px; top: 75px;
    width: 1080px; height: 630px;
    border-radius: 36px; overflow: hidden;
    background: radial-gradient(ellipse at 35% 30%, var(--card-charcoal), var(--card-black) 70%);
    box-shadow: 0 14px 30px rgba(0,0,0,0.25);
    font-family: "Open Sans", Arial, sans-serif;
  }
  .brand-name {
    position: absolute; left: 120px; top: 110px;
    font-family: "Open Sans", Arial, sans-serif; font-weight: 600;
    font-size: 56px; line-height: 1.1;
    color: var(--gold);
  }
  .owner {
    position: absolute; right: 668px; top: 268px;
    text-align: right; color: var(--text-muted);
    font-size: 24px; line-height: 1.35;
  }
  .owner .name { color: var(--gold); font-weight: 600; font-size: 28px; }
  .owner .role { margin-bottom: 26px; color: var(--white); }
  .divider {
    position: absolute; left: 432px; top: 262px;
    width: 2px; height: 190px; background: var(--silver); opacity: 0.8;
  }
  .contacts {
    position: absolute; left: 458px; top: 256px;
    list-style: none; color: var(--white); font-size: 24px;
  }
  .contacts li { display: flex; align-items: center; height: 40px; gap: 14px; }
  .contacts svg { width: 24px; height: 24px; flex: none; }
  .swoosh { position: absolute; left: 0; bottom: 0; width: 1080px; height: 200px; }
</style>
</head>
<body>
  <div class="card">
    <div class="brand-name">Maple Ridge Landscaping</div>

    <div class="owner">
      <div class="name">Derek Holt</div>
      <div class="role">Owner/Operator</div>
      <div>P.O. Box 917</div>
      <div>Cedar Cove, NL B2K 3M5</div>
    </div>

    <div class="divider"></div>

    <ul class="contacts">
      <li>
        <svg viewBox="0 0 24 24"><path fill="var(--gold)" d="M6 2h4l2 5-3 2a12 12 0 0 0 6 6l2-3 5 2v4c0 1-1 2-2 2A18 18 0 0 1 4 4c0-1 1-2 2-2z"/></svg>
        (709) 555-0142
      </li>
      <li>
        <svg viewBox="0 0 24 24"><rect x="6" y="1" width="12" height="22" rx="2" fill="var(--gold)"/><rect x="8" y="4" width="8" height="13" fill="var(--card-black)"/><circle cx="12" cy="20" r="1.3" fill="var(--card-black)"/></svg>
        (709) 555-0187
      </li>
      <li>
        <svg viewBox="0 0 24 24"><rect x="1" y="5" width="22" height="14" rx="1" fill="var(--gold)"/><path d="M2 6l10 7 10-7" fill="none" stroke="var(--card-black)" stroke-width="2"/></svg>
        mapleridgelndscpg@inboxmail.example
      </li>
      <li>
        <svg viewBox="0 0 24 24"><circle cx="12" cy="12" r="10" fill="none" stroke="var(--gold)" stroke-width="2"/><ellipse cx="12" cy="12" rx="4.5" ry="10" fill="none" stroke="var(--gold)" stroke-width="2"/><path d="M2 12h20" stroke="var(--gold)" stroke-width="2"/></svg>
        http://maple-ridge-lawncare.example
      </li>
    </ul>

    <svg class="swoosh" viewBox="0 0 1080 200" preserveAspectRatio="none" aria-hidden="true">
      <defs>
        <linearGradient id="goldBand" x1="0" y1="0" x2="1" y2="0">
          <stop offset="0" stop-color="var(--gold-deep)"/>
          <stop offset="0.45" stop-color="var(--gold-light)"/>
          <stop offset="1" stop-color="var(--gold)"/>
        </linearGradient>
      </defs>
      <path d="M0 105 Q540 150 1080 10 L1080 40 Q540 175 0 128 Z" fill="var(--silver)"/>
      <path d="M0 128 Q540 175 1080 40 L1080 200 L0 200 Z" fill="url(#goldBand)"/>
    </svg>
  </div>
</body>
</html>
```